Simple Business Cards for Self-employed Coach

Simple business card with a design that includes the QLT logo.
Using either only the logo color or additional colors that match the logo.

Meridian Guides reach deeply into the past, gathering wisdom from East and West, while still staying current with the frontiers of new discovery in cognitive science, genetics, and other disciplines. see https://www.brightharborpath.example/what-is-integral-coaching/

Target Market(s)

Coaching Clients in Tokyo /Asia; in business organizations, but also outside

Industry/Entity Type

Life Coaching

Contact Information for Business Card

Lukas Brenning
Certified Meridian Guide

3-2-48 Kamiyoshi
Nakarino 164-0392
Tokyo, Japan

Phone: +81 70 4817 5062
E-Mail: lukas.brenning@mailora.example

Font styles to use
Sans Serif

Colors
00a990

Requirements
Must have
• include uploaded logo
• color fitting with QLT logo color
Nice to have
• simple, elegant design
Should not have
• clutter

```html
<!DOCTYPE html>
<html lang="en">
<head>
<meta charset="utf-8">
<title>QLT – Business Card for Lukas Brenning</title>
<link rel="stylesheet" href="https://fonts.googleapis.com/css2?family=Lato:ital,wght@0,400;0,700;1,400&display=swap">
<style>
  :root {
    --teal: #127c6f;
    --teal-dark: #0e6e62;
    --ink: #2b2b2b;
    --rule: #c9c9c9;
    --paper: #ffffff;
    --backdrop: #f1f1f1;
  }
  * { box-sizing: border-box; margin: 0; padding: 0; }
  html, body {
    width: 865px; height: 1200px; overflow: hidden;
    background: var(--backdrop);
    font-family: "Lato", Arial, sans-serif;
  }
  .canvas { position: relative; width: 865px; height: 1200px; }
  .card {
    position: absolute; left: 51px; top: 382px;
    width: 763px; height: 436px;
    background: var(--paper);
    box-shadow: 6px 8px 14px rgba(0,0,0,0.28);
  }
  .brand {
    position: absolute; left: 63px; top: 180px;
    display: flex; align-items: center; gap: 18px;
    color: var(--teal);
  }
  .brand-square { width: 62px; height: 62px; background: var(--teal); }
  .brand-name {
    font-weight: 700; font-size: 80px; letter-spacing: 14px; line-height: 1;
  }
  .divider {
    position: absolute; left: 390px; top: 65px;
    width: 2px; height: 305px; background: var(--rule);
  }
  .name-band {
    position: absolute; left: 479px; top: 48px;
    width: 284px; height: 67px;
    background: linear-gradient(90deg, var(--teal), var(--teal-dark));
    color: #fff; padding: 6px 0 0 10px;
  }
  .person-name { font-size: 29px; font-weight: 400; line-height: 1.1; }
  .person-title { font-size: 14px; font-style: italic; margin-top: 2px; }
  .contact { position: absolute; left: 437px; top: 0; color: var(--ink); font-size: 19px; }
  .contact-row { position: absolute; left: 0; display: flex; gap: 16px; white-space: nowrap; }
  .contact-row svg { flex: none; width: 26px; height: 26px; }
  .contact-row p { line-height: 29px; }
  .row-email { top: 166px; }
  .row-address { top: 210px; }
  .row-address svg { margin-top: 30px; }
  .row-phone { top: 318px; }
</style>
</head>
<body>
<main class="canvas">
  <section class="card">
    <div class="brand">
      <span class="brand-square"></span>
      <span class="brand-name">QLT</span>
    </div>

    <div class="divider"></div>

    <header class="name-band">
      <h1 class="person-name">Lukas Brenning</h1>
      <p class="person-title">Certified Meridian Guide</p>
    </header>

    <div class="contact">
      <div class="contact-row row-email">
        <svg viewBox="0 0 26 26" aria-hidden="true">
          <circle cx="13" cy="13" r="13" fill="var(--teal)"/>
          <rect x="7" y="8.5" width="12" height="9" fill="#fff"/>
          <path d="M7 8.5 L13 13.5 L19 8.5" fill="none" stroke="var(--teal)" stroke-width="1.4"/>
        </svg>
        <p>lukas.brenning@mailora.example</p>
      </div>
      <div class="contact-row row-address">
        <svg viewBox="0 0 26 26" aria-hidden="true">
          <circle cx="13" cy="13" r="13" fill="var(--teal)"/>
          <path d="M13 20 C9 15 8.5 13 8.5 11.5 A4.5 4.5 0 0 1 17.5 11.5 C17.5 13 17 15 13 20 Z" fill="#fff"/>
          <circle cx="13" cy="11.5" r="1.8" fill="var(--teal)"/>
        </svg>
        <p>3-2-48 Kamiyoshi<br>Nakarino 164-0392<br>Tokyo, Japan</p>
      </div>
      <div class="contact-row row-phone">
        <svg viewBox="0 0 26 26" aria-hidden="true">
          <circle cx="13" cy="13" r="13" fill="var(--teal)"/>
          <path d="M9.5 7.5 L11.5 7.5 L12.5 10.5 L11 11.8 C11.8 13.5 12.6 14.3 14.2 15 L15.5 13.5 L18.5 14.5 L18.5 16.5 C18.5 17.5 17.5 18.5 16.5 18.5 C11.5 18.2 7.8 14.5 7.5 9.5 C7.5 8.5 8.5 7.5 9.5 7.5 Z" fill="#fff"/>
        </svg>
        <p>+81 70 4817 5062</p>
      </div>
    </div>
  </section>
</main>
</body>
</html>
```